Business card design needed

I have started a new business called Marlow Auto Electrical, although the words Marlow Auto Electrical will be used on signage and documents I actually want to market the business as MAE. The services I offer are Mobile Auto Electrical, Automotive Air Conditioning and Test And Tag. My business will be targetting the Mining Industry, Civil, Rail, Agricultural and Workshop Testing And Tagging. My auto electrical service ranges from fault finding to new vehicle and mine compliance fit outs. I have a very strong focus on quality workmanship. I will upload the logo I have designed and want to use I am happy for the logo colour to change but the design itself must stay the same. I want the design to have a modern, eye catching, energetic feel. As I am a passionate motorsport fan I am happy for this to also influence the design. I am happy for the front of the card to have only the emblem and logo design and the back to have all the info.

Industry/Entity Type

Electrical

Contact Information for Business Card

MAE Marlow Auto Electrical, Dale Penrick, Auto Electrician, Mobile No 0417263859

Requirements
Must have
• On the business card it is mandatory that the following license numbers are shown:

MVRL38462
VDA L071348
ABN 61 839 204 518

```html
<!DOCTYPE html>
<html lang="en">
<head>
<meta charset="utf-8">
<title>MAE – Marlow Auto Electrical Business Card</title>
<link href="https://fonts.googleapis.com/css2?family=Russo+One&family=Questrial&display=swap" rel="stylesheet">
<style>
  :root {
    --backdrop: #e6e6e4;
    --card-yellow: #e9c400;
    --card-white: #f7f7f5;
    --ink: #151515;
    --name-white: #ffffff;
    --rule-light: #f6ea9c;
    --mark-yellow: #d9b800;
  }
  * { margin: 0; padding: 0; box-sizing: border-box; }
  html, body {
    width: 1200px;
    height: 1000px;
    overflow: hidden;
    background: var(--backdrop);
  }
  .canvas {
    position: relative;
    width: 1200px;
    height: 1000px;
  }
  .card {
    position: absolute;
    width: 700px;
    height: 400px;
    box-shadow: 0 2px 6px rgba(0,0,0,0.15);
  }

  /* Back of card: contact details */
  .card-back {
    left: 420px;
    top: 80px;
    background: var(--card-yellow);
  }
  .card-back .business-name {
    position: absolute;
    right: 40px;
    top: 52px;
    font-family: "Russo One", sans-serif;
    font-weight: 400;
    font-size: 38px;
    letter-spacing: 1px;
    color: var(--ink);
    text-transform: uppercase;
    white-space: nowrap;
  }
  .card-back .heading-rule {
    position: absolute;
    left: 40px;
    right: 40px;
    top: 116px;
    height: 2px;
    background: var(--rule-light);
  }
  .card-back .contact {
    position: absolute;
    right: 40px;
    top: 146px;
    text-align: right;
  }
  .card-back .person-name {
    font-family: "Russo One", sans-serif;
    font-style: italic;
    font-size: 34px;
    color: var(--name-white);
    letter-spacing: 1px;
    line-height: 1.2;
  }
  .card-back .role,
  .card-back .mobile {
    font-family: "Questrial", sans-serif;
    font-size: 25px;
    color: var(--ink);
    line-height: 1.5;
  }
  .card-back .mobile { margin-top: 14px; }
  .card-back .licences {
    position: absolute;
    left: 40px;
    bottom: 30px;
    list-style: none;
    font-family: "Questrial", sans-serif;
    font-size: 17px;
    line-height: 1.5;
    color: var(--ink);
  }

  /* Front of card: marketing name */
  .card-front {
    left: 80px;
    top: 530px;
    background: var(--card-white);
    display: flex;
    align-items: center;
    justify-content: center;
    gap: 22px;
  }
  .card-front .brand-square {
    width: 84px;
    height: 84px;
    background: var(--mark-yellow);
  }
  .card-front .brand-lockup {
    display: flex;
    flex-direction: column;
    font-family: "Russo One", sans-serif;
    font-weight: 400;
    color: var(--ink);
    text-transform: uppercase;
  }
  .card-front .brand-initials {
    font-size: 96px;
    line-height: 1;
    letter-spacing: 4px;
  }
  .card-front .brand-name {
    font-size: 22px;
    letter-spacing: 1px;
    margin-top: 6px;
    white-space: nowrap;
  }
</style>
</head>
<body>
<main class="canvas">
  <section class="card card-back" aria-label="Card back">
    <h1 class="business-name">Marlow Auto Electrical</h1>
    <div class="heading-rule"></div>
    <div class="contact">
      <p class="person-name">Dale Penrick</p>
      <p class="role">Auto Electrician</p>
      <p class="mobile">Mobile No 0417263859</p>
    </div>
    <ul class="licences">
      <li>MVRL38462</li>
      <li>VDA L071348</li>
      <li>ABN 61 839 204 518</li>
    </ul>
  </section>

  <section class="card card-front" aria-label="Card front">
    <span class="brand-square"></span>
    <div class="brand-lockup">
      <span class="brand-initials">MAE</span>
      <span class="brand-name">Marlow Auto Electrical</span>
    </div>
  </section>
</main>
</body>
</html>
```